Summer Drinks Flyer for Coffee Shop

We are a coffee shop in London and would like to have a cool and nice flyer for our summer drinks (juices and frozen drink) flyer - see on the attached file for the list

Attached you can find an "attempt" - please note that I would no necessary need the image below.

I also attache our new logo.

thank you

Industry/Entity Type

Coffee Shop

```html
<!DOCTYPE html>
<html lang="en">
<head>
<meta charset="utf-8">
<title>New Summer Drinks Menu</title>
<link rel="stylesheet" href="https://fonts.googleapis.com/css2?family=Alfa+Slab+One&family=Bungee+Outline&family=Josefin+Sans:wght@400;600&family=Righteous&family=Yanone+Kaffeesatz:wght@300;400&display=swap">
<style>
  :root {
    --page-bg: #ffffff;
    --canvas-bg: #ffffff;
    --title-brown: #b95a27;
    --title-outline: #5a2a10;
    --accent-orange: #c8642e;
    --ink-blue: #2d3f9e;
    --gold: #c49a35;
    --gold-soft: #e6cf96;
    --gold-pale: #f6ecd2;
  }
  * { box-sizing: border-box; margin: 0; padding: 0; }
  html, body {
    width: 1200px; height: 1000px; overflow: hidden;
    background: var(--canvas-bg);
  }
  .flyer { position: relative; width: 1200px; height: 1000px; }
  .sheet {
    position: absolute; left: 262px; top: 48px; width: 676px; height: 902px;
    background: var(--page-bg);
    border: 1px solid #e4e4e4;
    box-shadow: 3px 4px 6px rgba(0,0,0,.25);
  }
  .border-ornament {
    position: absolute; top: 52px; width: 38px; height: 893px;
    background: linear-gradient(180deg, var(--gold-pale), var(--gold-soft) 50%, var(--gold-pale));
    border-radius: 4px;
    opacity: .7;
  }
  .border-ornament.left { left: 265px; }
  .border-ornament.right { left: 897px; }

  .headline {
    position: absolute; left: 262px; width: 676px; top: 78px;
    text-align: center; white-space: nowrap;
    font-family: "Alfa Slab One", serif; font-weight: 400;
    font-size: 40px; line-height: 1.1; color: var(--title-brown);
    -webkit-text-stroke: .6px var(--title-outline);
  }
  .subhead {
    position: absolute; left: 262px; width: 676px; top: 140px;
    text-align: center; white-space: nowrap;
    font-family: "Bungee Outline", sans-serif;
    font-size: 32px; line-height: 1.1; color: var(--accent-orange);
    -webkit-text-stroke: .8px var(--accent-orange);
    letter-spacing: 1px;
  }

  .menu-section { position: absolute; left: 0; top: 0; width: 1200px; height: 1000px; }
  .frame-lines {
    position: absolute; left: 310px; width: 578px;
    border: 1px solid var(--gold); border-radius: 14px;
  }
  .frame-lines::before, .frame-lines::after {
    content: ""; position: absolute; border: 1px solid var(--gold); border-radius: 12px;
  }
  .frame-lines::before { inset: 4px; }
  .frame-lines::after { inset: 8px; }
  .frame-glow {
    position: absolute; left: 305px; width: 588px;
    border: 4px solid var(--gold); border-radius: 20px;
    box-shadow: 0 0 6px 1px rgba(196,154,53,.55), inset 0 0 5px rgba(196,154,53,.45);
  }
  .section-title, .price, .offer, .item { white-space: nowrap; line-height: 1; }
  .section-title {
    position: absolute; left: 363px;
    font-family: "Josefin Sans", sans-serif; font-weight: 400;
    font-size: 23px; color: var(--ink-blue); letter-spacing: .5px;
  }
  .price {
    position: absolute; left: 740px;
    font-family: "Josefin Sans", sans-serif; font-weight: 400;
    font-size: 29px; color: var(--accent-orange); letter-spacing: 1px;
  }
  .offer {
    position: absolute; padding: 0 3px;
    background: var(--page-bg);
    font-family: "Righteous", sans-serif;
    font-size: 13px; color: var(--gold); letter-spacing: 1.5px;
  }
  .item {
    position: absolute;
    font-family: "Yanone Kaffeesatz", sans-serif;
    font-weight: 300; font-size: 21px;
  }
  .item.warm { color: var(--accent-orange); }
  .item.cool { color: var(--ink-blue); }

  .brand-name {
    position: absolute; left: 262px; width: 676px; top: 840px;
    text-align: center; white-space: nowrap;
    font-family: "Josefin Sans", sans-serif;
    font-weight: 400; font-size: 62px; line-height: 1; color: var(--gold);
    letter-spacing: 1px;
  }
</style>
</head>
<body>
<main class="flyer">
  <div class="sheet"></div>
  <div class="border-ornament left" role="img" aria-label="Gold scroll ornament border running down the left edge"></div>
  <div class="border-ornament right" role="img" aria-label="Gold scroll ornament border running down the right edge"></div>

  <h1 class="headline">New Summer Drinks</h1>
  <p class="subhead">MENU</p>

  <section class="menu-section">
    <div class="frame-lines" style="top:250px;height:102px"></div>
    <div class="frame-glow" style="top:203px;height:135px"></div>
    <h2 class="section-title" style="top:219px">FROZEN FRUIT DRINKS</h2>
    <span class="price" style="top:213px">£ 2.95</span>
    <span class="item warm" style="left:365px;top:275px">Strawberry and Banana</span>
    <span class="item cool" style="left:365px;top:302px">Pineapple, Mango and Banana</span>
  </section>

  <section class="menu-section">
    <div class="frame-lines" style="top:432px;height:146px"></div>
    <div class="frame-glow" style="top:382px;height:175px"></div>
    <h2 class="section-title" style="top:401px">FRUIT JUICES</h2>
    <span class="price" style="top:396px">£ 2.95</span>
    <span class="offer" style="left:552px;top:433px">ADD MINT OR GINGER FOR FREE!</span>
    <span class="item warm" style="left:363px;top:463px">Orange and Carrot</span>
    <span class="item cool" style="left:363px;top:490px">Orange and Pineapple</span>
    <span class="item warm" style="left:363px;top:517px">Pineapple&nbsp; and Apple</span>
    <span class="item cool" style="left:615px;top:474px">Apple and Kiwi</span>
    <span class="item warm" style="left:615px;top:501px">Carrot and Ginger</span>
  </section>

  <section class="menu-section">
    <div class="frame-lines" style="top:650px;height:108px"></div>
    <div class="frame-glow" style="top:603px;height:138px"></div>
    <h2 class="section-title" style="top:621px">ICED - COFFEES</h2>
    <span class="price" style="top:616px">£ 2.45</span>
    <span class="offer" style="left:614px;top:651px">ADD SYRUP SHOT FOR 10P</span>
    <span class="item warm" style="left:363px;top:677px">Iced Coffee</span>
    <span class="item cool" style="left:363px;top:704px">Iced Latte</span>
    <span class="item cool" style="left:615px;top:688px">Iced Chocolate Drink</span>
  </section>

  <p class="brand-name">Zuccherina</p>
</main>
</body>
</html>
```